Wordpress Fashion Website

Please see attached:
1) Our detailed design document.
2) Velvet Lane Wardrobe logo.
3) 20 images to be used as tiles in the homepage design.
Of importance to us is:
1) That our 'Unique Selling Point' of selling fashion based on your preferred style is immediately understood by the user.
2) The site is very aesthetically pleasing and appeals to the fashion conscious woman.
3) Clean design and SEO friendly.
4) Some of the style tiles can be seen in the homepage screenshot.
The design specification document should be used as a guideline. Please use your creativity and expertise to deviate from this as you wish. We look forward to seeing your submissions!
Gareth
Updates
We very much like this design and would welcome submissions along these lines also: http://www.kemrolu.qc.ca/fr/ Added Friday, December 19, 2014
Industry/Entity Type
Fashion
Look and feel
Each slider illustrates characteristics of the customer's brand and the style your logo design should communicate.

```html
<!DOCTYPE html>
<html lang="en">
<head>
<meta charset="utf-8">
<title>Velvet Lane Wardrobe – About Us</title>
<link rel="stylesheet" href="https://fonts.googleapis.com/css2?family=Roboto:wght@300;400;500&display=swap">
<style>
:root{
  --page:#e3e3e3;
  --panel:#ffffff;
  --side-dark:#2b3439;
  --side-darker:#232b30;
  --nav-line:#343e44;
  --nav-text:#5f6d74;
  --teal:#22aeae;
  --heading:#2e3336;
  --body-text:#9a9a9a;
  --rule:#e2e2e2;
  --foot-text:#8b959a;
}
*{margin:0;padding:0;box-sizing:border-box}
html,body{width:1200px;height:754px;overflow:hidden}
body{background:var(--page);font-family:'Roboto',sans-serif;position:relative}

.sidebar{position:absolute;left:0;top:0;width:257px;height:754px;background:var(--side-darker);box-shadow:2px 0 8px rgba(0,0,0,.25)}
.brand{height:184px;background:#fff;display:flex;flex-direction:column;align-items:center;justify-content:center;gap:12px}
.brand-mark{width:34px;height:34px;border-radius:50%;background:var(--heading)}
.brand-name{font-size:19px;font-weight:400;color:var(--heading);letter-spacing:.5px;text-transform:uppercase;text-align:center;line-height:1.2}

.nav{list-style:none}
.nav li{height:53.2px;border-bottom:1px solid var(--nav-line);background:var(--side-dark);display:flex;align-items:center;padding-left:55px;font-size:14px;color:var(--nav-text);text-transform:uppercase}
.nav li.active{background:var(--teal);color:#fff;border-bottom-color:var(--teal)}
.nav li.search{padding-right:0;justify-content:space-between}
.search-btn{width:55px;height:100%;background:var(--teal);display:flex;align-items:center;justify-content:center}

.account{position:absolute;left:47px;top:627px;display:flex;align-items:center;font-size:11px;color:var(--foot-text)}
.account .login{color:var(--teal)}
.account .sep{margin:0 5px}
.account .cart{margin-left:14px;margin-right:6px}
.account .count{color:var(--teal);margin-left:3px}
.social{position:absolute;left:48px;top:661px;display:flex;gap:9px}
.social span{width:20px;height:20px;border-radius:2px;background:#3e4a51}
.legal{position:absolute;left:48px;top:697px;font-size:10.5px;line-height:18px;color:var(--foot-text)}

.content{position:absolute;left:274px;top:17px;width:909px;height:720px;background:var(--panel)}
.section-title{position:absolute;left:26px;font-size:16px;font-weight:400;color:var(--heading);text-transform:uppercase}
.intro-title{top:24px}
.intro-photo{position:absolute;left:26px;top:58px;width:415px;height:258px;border:1px solid #dedede;padding:4px}
.intro-photo div{width:100%;height:100%;background:linear-gradient(90deg,#b9c3cc 0%,#d8d3cc 35%,#e48a6c 55%,#dfd8d2 75%,#eceae6 100%)}
.intro-text{position:absolute;left:466px;top:68px;width:420px;font-size:13.6px;font-weight:300;line-height:24px;color:var(--body-text)}
.intro-text p+p{margin-top:24px}
.rule{position:absolute;left:26px;top:358px;width:857px;height:1px;background:var(--rule)}

.about-title{top:410px}
.carousel-nav{position:absolute;left:813px;top:402px;display:flex;gap:2px}
.carousel-nav span{width:34px;height:34px;background:var(--teal);display:flex;align-items:center;justify-content:center}
.styles{position:absolute;left:26px;top:445px;display:flex;gap:11px}
.style-tile{width:206px;height:188px;position:relative}
.style-tile .photo{position:absolute;inset:0}
.style-tile .shade{position:absolute;inset:0;background:rgba(40,40,40,.45)}
.style-tile .label{position:absolute;left:0;right:0;top:72px;text-align:center;color:#fff;font-size:16px;font-weight:300}
.style-tile .label::after{content:"";display:block;width:92px;height:1px;background:#fff;margin:8px auto 0}
.boho{background:linear-gradient(180deg,#8f8576,#bdb5aa 50%,#7d776d)}
.casual{background:linear-gradient(180deg,#c9c6c2,#a8a6a4 50%,#4d5d72)}
.chic{background:linear-gradient(90deg,#b6bfc8,#e48a6c 55%,#d7d2cc)}
.formal{background:linear-gradient(180deg,#e6d2a8,#d9cfc2 45%,#2f5f96)}
</style>
</head>
<body>
<aside class="sidebar">
  <div class="brand">
    <span class="brand-mark"></span>
    <span class="brand-name">Velvet Lane Wardrobe</span>
  </div>
  <ul class="nav">
    <li>Home</li>
    <li class="active">About Us</li>
    <li>Products</li>
    <li>Editors Pics</li>
    <li>Selected Style Items</li>
    <li>Specials</li>
    <li>Contact Us</li>
    <li class="search">Search
      <span class="search-btn"><svg width="17" height="17" viewBox="0 0 17 17"><circle cx="6.5" cy="6.5" r="5" fill="none" stroke="#fff" stroke-width="2"/><line x1="10" y1="10" x2="15.5" y2="15.5" stroke="#fff" stroke-width="2.4" stroke-linecap="round"/></svg></span>
    </li>
  </ul>
  <div class="account">
    <span class="login">Log In</span><span class="sep">/</span><span>Sign in</span>
    <svg class="cart" width="22" height="18" viewBox="0 0 22 18"><path d="M1 2h3l3 10h11l2-7H6" fill="none" stroke="#22aeae" stroke-width="1.6"/><line x1="7" y1="8" x2="19" y2="8" stroke="#22aeae" stroke-width="1.2"/><circle cx="9" cy="15.5" r="1.6" fill="#22aeae"/><circle cx="16" cy="15.5" r="1.6" fill="#22aeae"/></svg>
    <span>Shopping</span><span class="count">(0)</span>
  </div>
  <div class="social"><span></span><span></span><span></span><span></span><span></span><span></span></div>
  <p class="legal">© 2014 Velvet Lane Wardrobe, All Rights Reserved<br>Designed &amp; Developed By Studiofold</p>
</aside>

<main class="content">
  <h2 class="section-title intro-title">Who are we?</h2>
  <figure class="intro-photo"><div role="img" aria-label="Woman in a coral top and pearl necklace on a bright street"></div></figure>
  <div class="intro-text">
    <p>Sed non mauris vitae erat consequat auctor eu in elit. Class aptent taciti sociosqu ad litora torquent per conubia nostra, per inceptos himenaeos. Mauris in erat justo. Nullam ac urna eu felis dapibus condimentum sit amet a augue. Sed non neque elit. Sed ut imperdiet nisi. Proin condimentum fermentum nunc.</p>
    <p>Sed non mauris vitae erat consequat auctor eu in elit. Class aptent taciti sociosqu ad litora torquent per conubia nostra, per inceptos himenaeos. Mauris in erat justo. Nullam ac urna eu felis dapibus condimentum sit amet a augue. Sed non neque elit. Sed ut imperdiet nisi. Proin condimentum fermentum nunc.</p>
  </div>
  <div class="rule"></div>

  <h2 class="section-title about-title">About Us</h2>
  <div class="carousel-nav">
    <span><svg width="10" height="14" viewBox="0 0 10 14"><path d="M8 1L2 7l6 6" fill="none" stroke="#fff" stroke-width="2.4"/></svg></span>
    <span><svg width="10" height="14" viewBox="0 0 10 14"><path d="M2 1l6 6-6 6" fill="none" stroke="#fff" stroke-width="2.4"/></svg></span>
  </div>
  <div class="styles">
    <div class="style-tile"><div class="photo boho" role="img" aria-label="Model in a white boho dress"></div><div class="shade"></div><span class="label">Boho-Chic</span></div>
    <div class="style-tile"><div class="photo casual" role="img" aria-label="Model in a tank top and jeans"></div><div class="shade"></div><span class="label">Casual</span></div>
    <div class="style-tile"><div class="photo chic" role="img" aria-label="Model in a coral top with pearls"></div><div class="shade"></div><span class="label">Chic</span></div>
    <div class="style-tile"><div class="photo formal" role="img" aria-label="Model in a blue strapless gown"></div><div class="shade"></div><span class="label">Formal</span></div>
  </div>
</main>
</body>
</html>
```